New 3 page ( front /back, so six total) company corporate brochure

We have an upcoming trade show in August, and we want a new corporate brochure that explains what TRN does, the brands we represent, the services we offer, and that makes TRN easy for your clients to do business with. We have two brochures that I'm uploading now for inspiration, along with our trade-show artwork, so you can get a feel for the theming. The brochure titled "AI brochure" is a version I made on chat that I like, but it needs better pics and not AI-made ones. One must have a page in the brochure to display the brand's rep. Thanks for helping us!

Target Market(s)

engineers and operators

Industry/Entity Type

water, wastewater and industrial pumps and liquid process equipment

Requirements
Must have
• 3 pages front back, six total printed pages. One page to display the brand logos and categories we represe

```html
<!DOCTYPE html>
<html lang="en">
<head>
<meta charset="utf-8">
<title>TRN Corporate Brochure</title>
<link href="https://fonts.googleapis.com/css2?family=Montserrat:wght@400;500;600;700;800&display=swap" rel="stylesheet">
<style>
  :root{
    --bg:#ebebeb;
    --blue:#1b6bbd;
    --blue-deep:#14579e;
    --black:#1c1e21;
    --panel:#2b2f36;
    --white:#ffffff;
    --ink:#1d2024;
    --muted:#d6dbe2;
    --fold:rgba(255,255,255,.14);
    --badge:#3a4048;
    --photo-steel-a:#c9d1da;
    --photo-steel-b:#5f86b8;
    --photo-machine-a:#3f6797;
    --photo-machine-b:#2a3b52;
    --photo-red-a:#d8322c;
    --photo-red-b:#8e1d1a;
  }
  *{box-sizing:border-box;margin:0;padding:0}
  html,body{width:1200px;height:1200px;overflow:hidden;background:var(--bg)}
  body{position:relative;font-family:"Montserrat",Arial,sans-serif;color:var(--white)}
  .sheet{position:absolute;left:226px;width:748px;height:530px;overflow:hidden;background:var(--white);box-shadow:0 2px 6px rgba(0,0,0,.18)}
  .sheet--outside{top:55px}
  .sheet--inside{top:614px}
  .sheet__inner{position:absolute;left:0;top:0;width:598px;height:424px;transform:scale(1.25);transform-origin:0 0}
  .shapes{position:absolute;left:0;top:0;width:598px;height:424px}
  .abs{position:absolute}

  /* outside spread: back panel, inside flap, cover */
  .capabilities{left:24px;top:32px;width:160px}
  .capabilities__title{font-size:13.5px;font-weight:700;line-height:1.22;letter-spacing:.2px;margin-bottom:24px}
  .capability{margin-bottom:10px}
  .capability__name{font-size:7.6px;font-weight:700;letter-spacing:.2px}
  .capability__text{font-size:6.1px;line-height:1.35;color:var(--muted)}
  .brand{right:28px;top:58px;font-size:30px;font-weight:800;color:var(--blue-deep);letter-spacing:1px;display:flex;align-items:center;gap:6px}
  .brand__dot{width:9px;height:9px;background:var(--blue-deep)}
  .headline{right:22px;top:228px;text-align:right;font-size:12.2px;font-weight:700;line-height:1.3}
  .headline__rule{right:40px;top:290px;width:98px;height:1px;background:rgba(255,255,255,.7)}
  .offer{left:418px;top:302px;width:158px;text-align:center;font-size:7.2px;font-weight:600;line-height:1.33}
  .contact{left:224px;top:290px;width:152px;text-align:center;font-size:5.8px;font-weight:500;line-height:1.4}
  .contact__icons{display:flex;justify-content:center;gap:5px;margin-bottom:12px}
  .contact p{margin-bottom:8px}
  .web{left:458px;top:400px;font-size:5.8px;font-weight:600}

  /* inside spread: three panels */
  .core{left:214px;top:18px}
  .core__title{font-size:12.2px;font-weight:700;line-height:1.3}
  .core__sub{font-size:5.6px;margin-top:6px;color:var(--muted)}
  .category-tag{left:211px;top:93px;background:var(--blue);padding:2px 5px;font-size:6.6px;font-weight:700}
  .list{font-size:5.6px;line-height:1.5;list-style:none}
  .list li::before{content:"• "}
  .list--pumps{left:214px;top:112px}
  .strengths{left:22px;top:100px;width:170px}
  .strength{margin-bottom:9px;font-size:5.8px;line-height:1.35;font-weight:600}
  .strength b{display:block;font-weight:700}
  .brand-row{left:22px;top:200px;display:flex;gap:5px}
  .brand-badge{width:28px;height:16px;border-radius:2px;background:var(--badge)}
  .dark{color:var(--ink)}
  .group-title{font-size:7px;font-weight:700}
  .blowers{left:312px;top:228px}
  .valves{left:213px;top:331px}
  .blowers .list,.valves .list{margin-top:7px}
  .fire{left:426px;top:158px;width:165px}
  .fire__section{margin-bottom:14px}
  .fire__title{font-size:7px;font-weight:700;margin-bottom:8px}
  .fire__text{font-size:5.6px;line-height:1.45}
  .fire .list{position:static}
</style>
</head>
<body>

<!-- Outside spread: panels 1–3 -->
<section class="sheet sheet--outside">
  <div class="sheet__inner">
    <svg class="shapes" viewBox="0 0 598 424">
      <defs>
        <linearGradient id="steel" x1="0" y1="0" x2="1" y2="1">
          <stop offset="0" stop-color="var(--photo-steel-a)"/>
          <stop offset="1" stop-color="var(--photo-steel-b)"/>
        </linearGradient>
        <linearGradient id="machine" x1="0" y1="0" x2="1" y2="1">
          <stop offset="0" stop-color="var(--photo-machine-a)"/>
          <stop offset="1" stop-color="var(--photo-machine-b)"/>
        </linearGradient>
      </defs>
      <rect x="0" y="0" width="199" height="294" fill="var(--panel)"/>
      <rect x="0" y="294" width="199" height="130" fill="url(#machine)" role="img" aria-label="Photo of a blue centrifugal pump being serviced on a workshop pallet"/>
      <rect x="199" y="0" width="399" height="310" fill="url(#steel)" role="img" aria-label="Photo of blue vertical multistage pumps installed in a plant room"/>
      <path d="M199,300 C300,300 420,272 485,228 C540,190 578,140 598,110 V424 H199 Z" fill="var(--blue)"/>
      <path d="M598,328 C565,378 500,410 410,424 H598 Z" fill="var(--black)"/>
      <path d="M598,392 C582,408 560,418 535,424 H598 Z" fill="var(--white)"/>
      <line class="fold" x1="398.5" y1="0" x2="398.5" y2="424" stroke="var(--fold)" stroke-width="0.6"/>
    </svg>

    <div class="abs capabilities">
      <h2 class="capabilities__title">FULL SERVICE<br>CAPABILITIES</h2>
      <div class="capability"><h3 class="capability__name">PREVENTIVE MAINTENANCE</h3><p class="capability__text">Scheduled maintenance programs to optimize equipment reliability and performance.</p></div>
      <div class="capability"><h3 class="capability__name">PUMP &amp; BLOWER REPAIR</h3><p class="capability__text">Expert repair for all major brands of pumps, blowers and rotating equipment.</p></div>
      <div class="capability"><h3 class="capability__name">FIELD SERVICE</h3><p class="capability__text">On-site troubleshooting, diagnostics and repair to get your equipment back online fast.</p></div>
      <div class="capability"><h3 class="capability__name">PARTS &amp; COMPONENTS</h3><p class="capability__text">Genuine OEM and premium replacement parts with fast turnaround.</p></div>
      <div class="capability"><h3 class="capability__name">SYSTEM OPTIMIZATION</h3><p class="capability__text">Performance evaluations and upgrades to improve efficiency and reduce operating costs.</p></div>
    </div>

    <div class="abs brand"><span class="brand__dot"></span>TRN</div>

    <h1 class="abs headline">FLUID HANDLING &amp;<br>PROCESS EQUIPMENT<br>SOLUTIONS</h1>
    <div class="abs headline__rule"></div>
    <p class="abs offer">PUMPS • BLOWERS<br>ENGINEERED SYSTEMS<br>AUTOMATION • VALVES<br>SERVICE &amp; REPAIR</p>

    <div class="abs contact">
      <div class="contact__icons">
        <svg width="8" height="9" viewBox="0 0 8 9"><path d="M4 0.5a3 3 0 0 1 3 3c0 2.2-3 5-3 5s-3-2.8-3-5a3 3 0 0 1 3-3z" fill="none" stroke="#fff" stroke-width="1"/><circle cx="4" cy="3.5" r="1" fill="#fff"/></svg>
        <svg width="8" height="9" viewBox="0 0 8 9"><path d="M1.5 1 L3 1 L3.6 2.8 L2.7 3.5 C3.2 4.7 4 5.5 5.2 6 L5.9 5.1 L7.5 5.7 V7.3 C4 7.5 1 4.5 1.5 1 Z" fill="#fff"/></svg>
        <svg width="9" height="9" viewBox="0 0 9 9"><rect x="0.5" y="2" width="8" height="5.5" fill="#fff"/><path d="M0.5 2 L4.5 5 L8.5 2" fill="none" stroke="var(--blue)" stroke-width="0.8"/></svg>
        <svg width="9" height="9" viewBox="0 0 9 9"><circle cx="4.5" cy="4.5" r="3.7" fill="none" stroke="#fff" stroke-width="0.8"/><ellipse cx="4.5" cy="4.5" rx="1.6" ry="3.7" fill="none" stroke="#fff" stroke-width="0.7"/><path d="M0.8 4.5 H8.2" stroke="#fff" stroke-width="0.7"/></svg>
      </div>
      <p>2400 Harbor Mill Rd.<br>Eastfield, VA 23900</p>
      <p>(555) 014-7200</p>
      <p>sales@trn-fluidsystems.com</p>
      <p>www.trn-fluidsystems.com</p>
    </div>
    <p class="abs web">www.trn-fluidsystems.com</p>
  </div>
</section>

<!-- Inside spread: panels 4–6 -->
<section class="sheet sheet--inside">
  <div class="sheet__inner">
    <svg class="shapes" viewBox="0 0 598 424">
      <defs>
        <linearGradient id="machine2" x1="0" y1="0" x2="1" y2="1">
          <stop offset="0" stop-color="var(--photo-machine-a)"/>
          <stop offset="1" stop-color="#6d7a86"/>
        </linearGradient>
        <linearGradient id="red" x1="0" y1="0" x2="1" y2="1">
          <stop offset="0" stop-color="var(--photo-red-a)"/>
          <stop offset="1" stop-color="var(--photo-red-b)"/>
        </linearGradient>
        <linearGradient id="blueprod" x1="0" y1="0" x2="1" y2="1">
          <stop offset="0" stop-color="#3a79c4"/>
          <stop offset="1" stop-color="#1d4f8c"/>
        </linearGradient>
      </defs>
      <rect width="598" height="424" fill="var(--blue)"/>
      <path d="M395,0 H598 V100 C500,100 420,122 380,172 V424 H199 V225 C330,190 390,90 395,0 Z" fill="var(--white)"/>
      <path d="M0,95 C90,90 170,50 210,0 H395 C390,90 330,190 199,225 H0 Z" fill="var(--black)"/>
      <rect x="0" y="225" width="199" height="199" fill="url(#machine2)" role="img" aria-label="Photo of two blue vertical pumps piped into a system"/>
      <rect x="301" y="97" width="65" height="53" fill="#f4f6f8"/>
      <rect x="306" y="105" width="55" height="38" rx="4" fill="url(#blueprod)" role="img" aria-label="Product image of a blue end suction pump"/>
      <rect x="404" y="5" width="174" height="107" rx="4" fill="url(#red)" role="img" aria-label="Product image of a red split case fire pump with motor"/>
      <rect x="202" y="235" width="100" height="57" fill="#f4f6f8"/>
      <rect x="208" y="243" width="88" height="42" rx="4" fill="url(#blueprod)" role="img" aria-label="Product image of a positive displacement blower package"/>
      <rect x="318" y="332" width="71" height="72" fill="#f4f6f8"/>
      <rect x="330" y="344" width="47" height="48" rx="6" fill="url(#blueprod)" role="img" aria-label="Product image of a blue electric valve actuator"/>
      <line class="fold" x1="199.5" y1="0" x2="199.5" y2="225" stroke="var(--fold)" stroke-width="0.6"/>
      <line class="fold" x1="398.5" y1="172" x2="398.5" y2="424" stroke="rgba(0,0,0,.08)" stroke-width="0.6"/>
    </svg>

    <div class="abs core">
      <h2 class="core__title">CORE EQUIPMENT<br>SOLUTIONS</h2>
      <p class="core__sub">High-Quality Products for Demanding Applications</p>
    </div>

    <div class="abs category-tag">PUMPS</div>
    <ul class="abs list list--pumps">
      <li>Centrifugal Pumps</li><li>End Suction</li><li>Split Case</li><li>Vertical Pumps</li>
      <li>Self-Priming</li><li>Magnetic Drive</li><li>Gear Pumps</li><li>Dosing / Metering Pumps</li>
    </ul>

    <div class="abs strengths">
      <p class="strength"><b>ENGINEERED SYSTEMS</b>Custom solutions built for your application</p>
      <p class="strength"><b>OEM PARTNERSHIPS</b>Representing the industry's leading brands</p>
      <p class="strength"><b>FAST TURNAROUND SERVICE</b>Minimize downtime and keep you running</p>
      <p class="strength"><b>LOCAL INVENTORY &amp; SUPPORT</b>Products on hand. People you can count on.</p>
    </div>

    <div class="abs brand-row" role="img" aria-label="Represented brand badges">
      <span class="brand-badge"></span><span class="brand-badge"></span><span class="brand-badge"></span><span class="brand-badge"></span><span class="brand-badge"></span>
    </div>

    <div class="abs blowers dark">
      <h3 class="group-title">BLOWERS</h3>
      <ul class="list">
        <li>Positive Displacement<br>&nbsp;&nbsp;(Roots-Type)</li><li>Rotary Lobe</li><li>Rotary Screw</li>
        <li>Centrifugal Blowers</li><li>Vacuum Blowers</li>
      </ul>
    </div>

    <div class="abs valves dark">
      <h3 class="group-title">VALVES &amp;<br>ACTUATION</h3>
      <ul class="list">
        <li>Ball Valves</li><li>Butterfly Valves</li><li>Gate, Globe &amp; Check Valves</li>
        <li>Actuators &amp; Positioners</li><li>Valve Automation</li>
      </ul>
    </div>

    <div class="abs fire">
      <div class="fire__section">
        <h3 class="fire__title">FIRE PROTECTION PUMP SYSTEMS</h3>
        <p class="fire__text">Complete Fire Pump Packages<br>&amp; Engineered Systems</p>
      </div>
      <div class="fire__section">
        <h3 class="fire__title">COMPLETE PACKAGES</h3>
        <ul class="list"><li>Fire Pumps</li><li>Jockey Pumps</li><li>Diesel &amp; Electric Drivers</li><li>Dosing / Metering Pumps</li></ul>
      </div>
      <div class="fire__section">
        <h3 class="fire__title">COMPONENTS</h3>
        <ul class="list"><li>Controllers &amp; Annunciators</li><li>Suction / Discharge Manifolds</li><li>Valves &amp; Accessories</li></ul>
      </div>
      <div class="fire__section">
        <h3 class="fire__title">SUPPORT</h3>
        <ul class="list"><li>Testing &amp; Certification</li><li>Service &amp; Repair</li><li>Replacement Parts</li></ul>
      </div>
    </div>
  </div>
</section>

</body>
</html>
```